Banner poster with different motifs

I'm looking for 5 banners and posters in A1 format in the same design, or the similarity must be recognizable...
Kept quite simple with different titles.

1 ballet
2 Contemporary Dance
3 high heels
4 Salsa & Bachata & Zouk
5 Hip Hop

Modern bright colors
it is for the entrance so that the students see here is a dance school

The text may also be included in the image
The photos are for guidance only; some are our own, some are purchased. However, we are permitted to use them, including our logo, of course.

```html
<!DOCTYPE html>
<html lang="en">
<head>
<meta charset="utf-8">
<title>High Heels – Dance Class Poster</title>
<link rel="stylesheet" href="https://fonts.googleapis.com/css2?family=Inter:wght@800&family=Montserrat:wght@300;400&display=swap">
<style>
  :root {
    --page: #ffffff;
    --ink: #ffffff;
    --night: #0c0b0e;
    --smoke-deep: #143a44;
    --smoke-teal: #1f6b7a;
    --smoke-cyan: #3fb7cc;
    --magenta: #f00fc0;
    --berry: #b0005f;
    --plum: #4e0c3e;
    --amber: #f2b415;
    --orange: #e5742c;
    --crimson: #d00022;
    --violet: #4a55d0;
    --aqua: #36b7cc;
  }
  * { margin: 0; padding: 0; box-sizing: border-box; }
  html, body {
    width: 1002px;
    height: 1200px;
    overflow: hidden;
    background: var(--page);
  }
  .poster {
    position: absolute;
    left: 77px;
    top: 0;
    width: 848px;
    height: 1200px;
    overflow: hidden;
    background: var(--night);
  }
  .poster__art {
    position: absolute;
    inset: 0;
    width: 100%;
    height: 100%;
    display: block;
  }
  .poster__title {
    position: absolute;
    top: 20px;
    left: 0;
    width: 100%;
    text-align: center;
    font-family: "Inter", "Helvetica Neue", Arial, sans-serif;
    font-weight: 800;
    font-size: 99px;
    letter-spacing: -3.5px;
    line-height: 1;
    color: var(--ink);
  }
  .brand {
    position: absolute;
    left: 563px;
    top: 978px;
    width: 280px;
    text-align: center;
    color: var(--ink);
    font-family: "Montserrat", Arial, sans-serif;
  }
  .brand__mark {
    width: 76px;
    height: 76px;
    margin: 0 auto 8px;
    border: 1.5px solid var(--ink);
    border-radius: 50%;
  }
  .brand__name {
    font-weight: 300;
    font-size: 31px;
    letter-spacing: 2px;
    line-height: 1;
  }
  .brand__tagline {
    margin-top: 9px;
    font-weight: 400;
    font-size: 9.5px;
    letter-spacing: 3.4px;
    line-height: 1.2;
  }
  .social {
    display: flex;
    justify-content: center;
    gap: 53px;
    margin-top: 11px;
  }
  .social__item {
    width: 32px;
    height: 32px;
    border-radius: 6px;
    background: var(--ink);
  }
</style>
</head>
<body>
  <main class="poster">
    <svg class="poster__art" viewBox="0 0 848 1200" xmlns="http://www.w3.org/2000/svg">
      <defs>
        <radialGradient id="smoke" cx="50%" cy="68%" r="55%">
          <stop offset="0" stop-color="var(--smoke-teal)" stop-opacity="0.85"/>
          <stop offset="0.55" stop-color="var(--smoke-deep)" stop-opacity="0.7"/>
          <stop offset="1" stop-color="var(--night)" stop-opacity="0"/>
        </radialGradient>
        <radialGradient id="glint">
          <stop offset="0" stop-color="#ffffff" stop-opacity="0.9"/>
          <stop offset="1" stop-color="#ffffff" stop-opacity="0"/>
        </radialGradient>
        <linearGradient id="cornerGlow" x1="0" y1="0" x2="1" y2="0">
          <stop offset="0" stop-color="var(--berry)"/>
          <stop offset="1" stop-color="var(--night)" stop-opacity="0"/>
        </linearGradient>
        <linearGradient id="pinkDome" x1="0" y1="0" x2="1" y2="0">
          <stop offset="0" stop-color="var(--magenta)"/>
          <stop offset="1" stop-color="var(--plum)"/>
        </linearGradient>
        <linearGradient id="amberDisc" x1="0" y1="0" x2="0" y2="1">
          <stop offset="0" stop-color="var(--amber)"/>
          <stop offset="0.6" stop-color="var(--orange)" stop-opacity="0.7"/>
          <stop offset="1" stop-color="var(--orange)" stop-opacity="0.25"/>
        </linearGradient>
        <linearGradient id="crimsonDisc" x1="0" y1="0" x2="0" y2="1">
          <stop offset="0" stop-color="var(--crimson)"/>
          <stop offset="1" stop-color="var(--violet)" stop-opacity="0.55"/>
        </linearGradient>
        <linearGradient id="plumPanel" x1="0" y1="0" x2="1" y2="1">
          <stop offset="0" stop-color="var(--plum)"/>
          <stop offset="1" stop-color="var(--berry)"/>
        </linearGradient>
        <clipPath id="panelClip">
          <polygon points="418,1200 848,767 848,1200"/>
        </clipPath>
      </defs>

      <rect width="848" height="1200" fill="var(--night)"/>
      <rect class="photo" width="848" height="1200" fill="url(#smoke)" role="img"
            aria-label="Photo: two dancers in black dancewear and platform high heels posing in teal stage smoke"/>

      <rect width="330" height="420" fill="url(#cornerGlow)" opacity="0.9"/>
      <circle cx="180" cy="300" r="220" fill="#000000" opacity="0.25"/>
      <ellipse cx="112" cy="224" rx="135" ry="66" fill="url(#pinkDome)"/>
      <circle cx="637" cy="335" r="240" fill="url(#amberDisc)" opacity="0.85"/>
      <circle cx="40" cy="714" r="255" fill="url(#crimsonDisc)" opacity="0.75"/>
      <circle cx="266" cy="1036" r="105" fill="var(--aqua)" opacity="0.35"/>

      <polygon points="848,130 848,290 0,1138 0,978" fill="#ffffff" opacity="0.06"/>
      <polygon points="848,440 848,520 0,1368 0,1288" fill="#000000" opacity="0.18"/>

      <g clip-path="url(#panelClip)">
        <rect x="400" y="760" width="448" height="440" fill="var(--plum)" opacity="0.55"/>
        <circle cx="723" cy="1188" r="300" fill="url(#plumPanel)"/>
      </g>

      <circle cx="765" cy="372" r="30" fill="url(#glint)"/>
      <circle cx="129" cy="1120" r="30" fill="url(#glint)"/>
      <circle cx="504" cy="1094" r="34" fill="url(#glint)"/>
    </svg>

    <h1 class="poster__title">High Heels</h1>

    <div class="brand">
      <div class="brand__mark"></div>
      <p class="brand__name">MOVIDANZA</p>
      <p class="brand__tagline">DANCE CENTER FRANKFURT</p>
      <div class="social">
        <span class="social__item"></span>
        <span class="social__item"></span>
        <span class="social__item"></span>
      </div>
    </div>
  </main>
</body>
</html>
```